General Surgeon flyer to be distributed to GPs

I am a general surgeon and I would like to have a flyer designed aiming to introduce myself to GPs.

Name: Dr Tobias Vanterpool MD, FRACS
Address: Suite 4C, Brindle private hospital, 518 Cobbler Parade, Wantirna, VIC, 3152
T: (03) 9587 1062
F: (03) 9316 4471
E: referrals@lanternoperativeclinic.com.au
Website: www.lanternoperativeclinic.com.au

Tobias is a highly trained general surgeon, having completed extensive surgical training at Coralbay health, Fenwick and Thornleigh Health networks. He further specialized by completing a fellowship in Oesophagogastric and Bariatric Surgery at Larkspur Hospital Northgate, one of Victoria’s leading Upper GI surgical centres.

With expertise in both advanced laparoscopic and open surgical techniques, he performs a wide range of procedures involving the gastrointestinal system, abdominal wall hernias, as well as other major and minor general surgical operations. In addition to holding appointments at Coralbay Health, he also operates at Brindle and Quarrydale Private Hospitals.

Dr Vanterpool is committed to providing patient-centred care with a focus on surgical precision, safety, and long-term health outcomes.

He is also Fluent in Greek/Italian.
Outside of surgery, Tobias enjoys playings jazz guitar and spending time with his 4-year-old Labrador on beach walks.

Upper GI & Bariatric Surgery:
Hiatus hernia repair, sleeve gastrectomy, gastric bypass
General Surgery conditions:
Gallbladder Surgery: Laparoscopic cholecystectomy
Hernia Repair: Laparoscopic and open surgery (inguinal,
umbilical, incisional)
Anorectal Procedures: Haemorrhoidectomy, haemorrhoid banding
Hand Surgery: Carpal tunnel release, Lymph Node Biopsy
Ingrown Toenail Surgery
Skin & Soft Tissue Surgery: Skin cancer removal, lipoma and
sebaceous cyst excision
Emergency Surgery: Laparotomy, Appendicectomy, bowel resection
Endoscopy: Diagnostic and therapeutic procedures

```html
<!DOCTYPE html>
<html lang="en">
<head>
<meta charset="utf-8">
<title>Dr Tobias Vanterpool – General Surgeon</title>
<link href="https://fonts.googleapis.com/css2?family=Archivo+Black&family=Arimo:wght@400;700&family=Montserrat:wght@500;600&display=swap" rel="stylesheet">
<style>
  :root{
    --navy:#0a55a8;
    --ink:#1a4fa0;
    --cyan:#0bbfee;
    --green:#4cb853;
    --white:#ffffff;
    --soft:#3a74c4;
    --badge:#c9d3e3;
  }
  html,body{margin:0;padding:0;width:846px;height:1200px;overflow:hidden;background:#e4e4e4;}
  .flyer{position:relative;width:846px;height:1200px;overflow:hidden;background:var(--navy);font-family:"Arimo",Arial,sans-serif;}
  .backdrop{position:absolute;inset:0;}
  .brand{position:absolute;left:68px;top:61px;width:174px;height:174px;border-radius:50%;background:var(--cyan);
    display:flex;align-items:center;justify-content:center;text-align:center;}
  .brand-name{font-family:"Arimo",Arial,sans-serif;font-weight:700;font-size:19px;line-height:23px;color:#0d2f66;}
  .doctor-title{position:absolute;left:50px;top:362px;width:370px;text-align:center;margin:0;
    font-family:"Archivo Black",Arial,sans-serif;font-weight:400;font-size:24px;line-height:28px;color:var(--ink);}
  .bio{position:absolute;left:42px;top:505px;width:438px;}
  .bio-main{background:var(--white);border-top-left-radius:32px;height:328px;box-sizing:border-box;padding:24px 12px 0 22px;}
  .bio-main p{margin:0 0 20px;font-weight:700;font-size:14.2px;line-height:20.3px;color:var(--ink);}
  .bio-personal{background:var(--green);border-bottom-right-radius:40px;height:111px;box-sizing:border-box;padding:22px 12px 0 22px;}
  .bio-personal p{margin:0;font-weight:700;font-size:14.2px;line-height:20.5px;color:var(--white);}
  .contact{position:absolute;left:46px;top:984px;width:434px;}
  .contact-name{margin:0;padding-bottom:4px;border-bottom:1.5px solid var(--green);font-weight:700;font-size:18px;color:var(--green);}
  .contact-list{list-style:none;margin:8px 0 0;padding:0;font-family:"Montserrat",Arial,sans-serif;font-weight:500;font-size:14.2px;color:var(--white);}
  .contact-list li{display:flex;align-items:flex-start;gap:5px;line-height:18px;margin-bottom:6px;}
  .contact-list svg{flex:0 0 13px;width:13px;height:13px;margin-top:2px;fill:var(--green);}
  .services{position:absolute;left:504px;top:497px;width:291px;}
  .service{position:relative;height:70px;}
  .service-box{position:absolute;left:0;right:0;top:16px;height:42px;border:1.5px solid var(--cyan);border-radius:22px;box-sizing:border-box;}
  .service-tag{position:absolute;left:47px;top:0;width:198px;height:27px;border-radius:14px;background:var(--cyan);
    font-weight:700;font-size:10.8px;line-height:27px;text-align:center;color:var(--ink);}
  .service-detail{position:absolute;left:8px;right:8px;top:31px;text-align:center;font-weight:700;font-size:11.4px;line-height:11px;color:var(--white);}
  .service-detail.single{top:37px;}
</style>
</head>
<body>
<main class="flyer">
  <svg class="backdrop" width="846" height="1200" viewBox="0 0 846 1200">
    <defs>
      <clipPath id="upperArea"><path d="M0,0 H846 V311 C560,540 250,500 0,368 Z"/></clipPath>
      <linearGradient id="portraitTone" x1="0" y1="0" x2="0" y2="1">
        <stop offset="0" stop-color="#2fb8e6"/>
        <stop offset="0.55" stop-color="#6f9fd6"/>
        <stop offset="1" stop-color="#1f3f82"/>
      </linearGradient>
    </defs>
    <path d="M520,700 C640,640 760,660 846,610 V900 C760,960 640,930 520,990 Z" fill="var(--soft)" opacity="0.45"/>
    <path d="M0,0 H846 V311 C560,540 250,500 0,368 Z" fill="var(--cyan)"/>
    <g clip-path="url(#upperArea)">
      <rect x="392" y="40" width="420" height="470" rx="60" fill="url(#portraitTone)" role="img" aria-label="Portrait photo of Dr Tobias Vanterpool in a navy suit and tie"/>
    </g>
    <path d="M0,368 C250,500 560,540 846,311" fill="none" stroke="var(--white)" stroke-width="2.5"/>
    <path d="M574,0 C500,230 290,332 0,330" fill="none" stroke="var(--white)" stroke-width="3"/>
    <path d="M0,0 H488 C440,220 260,320 0,316 Z" fill="var(--green)"/>
    <path d="M0,0 H405 C370,170 220,275 0,281 Z" fill="var(--white)"/>
    <path d="M400,1200 C520,1120 700,1085 846,1100" fill="none" stroke="var(--white)" stroke-width="2"/>
    <path d="M420,1200 C540,1130 700,1100 846,1114 V1200 Z" fill="var(--green)"/>
    <path d="M455,1200 C560,1145 710,1122 846,1132 V1200 Z" fill="var(--white)"/>
    <rect x="664" y="1158" width="22" height="22" rx="3" fill="var(--badge)"/>
    <circle cx="806" cy="1166" r="16" fill="var(--badge)"/>
  </svg>

  <div class="brand"><span class="brand-name">Lantern<br>Operative<br>Clinic</span></div>

  <h1 class="doctor-title">Dr Tobias Vanterpool<br>MD, FRACS</h1>

  <section class="bio">
    <div class="bio-main">
      <p>Tobias is a highly trained general surgeon, having completed extensive surgical training at Coralbay health, Fenwick and Thornleigh Health networks. He further specialized by completing a fellowship in Oesophagogastric and Bariatric Surgery at Larkspur Hospital Northgate, one of Victoria’s leading Upper GI surgical centres.</p>
      <p>With expertise in both advanced laparoscopic and open surgical techniques, he performs a wide range of procedures involving the gastrointestinal system, abdominal wall hernias, as well as other major and minor general surgical operations. In addition to holding appointments at Coralbay Health, he also operates at Brindle and Quarrydale Private Hospitals.</p>
    </div>
    <div class="bio-personal">
      <p>Fluent in Greek/Italian.<br>Outside of surgery, I enjoy playing jazz guitar and spending time with my 4-year-old Labrador on beach walks.</p>
    </div>
  </section>

  <section class="contact">
    <h2 class="contact-name">Dr Tobias Vanterpool MD, FRACS</h2>
    <ul class="contact-list">
      <li><svg viewBox="0 0 24 24"><path d="M12 1a8 8 0 0 0-8 8c0 6 8 14 8 14s8-8 8-14a8 8 0 0 0-8-8zm0 11a3 3 0 1 1 0-6 3 3 0 0 1 0 6z"/></svg><span>Suite 4C, Brindle private hospital, 518 Cobbler Parade, Harrowvale, VIC, 3199</span></li>
      <li><svg viewBox="0 0 24 24"><path d="M6.6 10.8a15 15 0 0 0 6.6 6.6l2.2-2.2a1 1 0 0 1 1-.25 11 11 0 0 0 3.6.6 1 1 0 0 1 1 1V20a1 1 0 0 1-1 1A17 17 0 0 1 3 4a1 1 0 0 1 1-1h3.5a1 1 0 0 1 1 1 11 11 0 0 0 .6 3.6 1 1 0 0 1-.25 1z"/></svg><span>(03) 9587 1062</span></li>
      <li><svg viewBox="0 0 24 24"><path d="M6.6 10.8a15 15 0 0 0 6.6 6.6l2.2-2.2a1 1 0 0 1 1-.25 11 11 0 0 0 3.6.6 1 1 0 0 1 1 1V20a1 1 0 0 1-1 1A17 17 0 0 1 3 4a1 1 0 0 1 1-1h3.5a1 1 0 0 1 1 1 11 11 0 0 0 .6 3.6 1 1 0 0 1-.25 1z"/></svg><span>(03) 9316 4471</span></li>
      <li><svg viewBox="0 0 24 24"><path d="M2 5h20v2l-10 6L2 7zm0 4l10 6 10-6v10H2z"/></svg><span>referrals@lanternoperativeclinic.com.au</span></li>
      <li><svg viewBox="0 0 24 24"><path d="M5 2l14 10-6 1.5 3.5 7-2.5 1.3-3.5-7L5 19z"/></svg><span>Website: www.lanternoperativeclinic.com.au</span></li>
    </ul>
  </section>

  <section class="services">
    <div class="service"><div class="service-box"></div><div class="service-tag">Upper GI &amp; Bariatric Surgery:</div><div class="service-detail">Hiatus hernia repair, sleeve gastrectomy,<br>gastric bypass</div></div>
    <div class="service"><div class="service-box"></div><div class="service-tag">General Surgery conditions:</div><div class="service-detail">Gallbladder Surgery: Laparoscopic<br>cholecystectomy</div></div>
    <div class="service"><div class="service-box"></div><div class="service-tag">Hernia Repair:</div><div class="service-detail">Laparoscopic and open surgery<br>(inguinal, umbilical, incisional)</div></div>
    <div class="service"><div class="service-box"></div><div class="service-tag">Anorectal Procedures:</div><div class="service-detail single">Haemorrhoidectomy, haemorrhoid banding</div></div>
    <div class="service"><div class="service-box"></div><div class="service-tag">Hand Surgery:</div><div class="service-detail">Carpal tunnel release, Lymph Node Biopsy<br>Ingrown Toenail Surgery</div></div>
    <div class="service"><div class="service-box"></div><div class="service-tag">Skin &amp; Soft Tissue Surgery:</div><div class="service-detail">Skin cancer removal, lipoma<br>and sebaceous cyst excision</div></div>
    <div class="service"><div class="service-box"></div><div class="service-tag">Emergency Surgery:</div><div class="service-detail">Laparotomy, Appendicectomy,<br>bowel resection</div></div>
    <div class="service"><div class="service-box"></div><div class="service-tag">Endoscopy:</div><div class="service-detail single">Diagnostic and therapeutic procedures</div></div>
  </section>
</main>
</body>
</html>
```